Book Cover - Easter Dot Book for Kids

Main Title (big text): Dot Markers Activity Book for Toddlers - Easter Edition  
Subtitle (smaller text/small banner at the bottom of cover): Pip-n-Stamp Children's Easter Books for Kids Ages 1-3, 2-4, 3-5 
NO AUTHOR.
Dimensions: 8.5 x 11 inches
FRONT AND BACK COVERS SEPARATELY / NO SPINE
FINAL FORMATS NEEDED: PDF, PNG, JPG (RGB & at least 300 DPI), and Ai/Vector + Layers/Fonts (You can zip the final files).

This is a children’s dot marker coloring book. Please make the cover kid-friendly, vibrant & colorful, and make sure to include the below details. I have also provided an example of what I want the cover to look like (labeled "EXAMPLE"), please remember this is just an example and should NOT be used or copied for the cover.  

Details: 
1. The title of the book should have this part: "I Dot You - Dot Markers Activity Book Valentine's Day Edition" in large and readable letters, while the rest of the title should be small and not take up too much space. The smaller part of the title can be a bottom banner, or something small and not distracting.  
2. The background graphics, if any, should not be super busy or too much going on. I like a simple and clean look, like the example attached.  
3. The dots on the attachments for the cover need to be colored like the example, as the child will be using dot markers for this activity book. 
4. Please use the attachments labeled "Option 1" or "Option 2" for the main cover image. Please combine both images uploaded together for the cover, as I want both the Easter Bunny and the basket with eggs. The attachment labeled "EXAMPLE" is just an example of how I want the cover to look, but should NOT be copied. 
5. This is an Easter book so the colors should reflect that. Pastel colors are best for Easter, please. I have uploaded some color palettes to help inspire you, but you are NOT limited to only the colors I uploaded. You can use other colors as long as it looks good in the Easter theme.

PLEASE USE ONLY ONE OF THE ATTACHMENTS FOR THE COVER, DO NOT USE BOTH ON ONE COVER. Please ask any questions if you need help understanding.

```html
<!DOCTYPE html>
<html lang="en">
<head>
<meta charset="utf-8">
<title>Dot Markers Activity Book for Toddlers – Easter Edition</title>
<link href="https://fonts.googleapis.com/css2?family=Luckiest+Guy&family=Fredoka:wght@600;700&display=swap" rel="stylesheet">
<style>
  :root {
    --stage: #e4e2e6;
    --paper: #f7f4f8;
    --title-pink: #ee3f9c;
    --title-navy: #1f2a6b;
    --band-pink: #e81e78;
    --band-text: #ffffff;
    --egg-blue: #2f8ee8;
    --egg-text: #1f2a6b;
    --dot-brown: #9b5a1e;
    --dot-teal: #5fd6cf;
    --dot-blush: #f5b7e0;
    --dot-salmon: #f3917e;
    --dot-green: #3fbf57;
    --dot-rust: #d9531b;
    --dot-pink: #f0149a;
    --dot-maroon: #8a1538;
    --dot-blue: #2f7ff0;
    --dot-red: #f0141e;
    --dot-purple: #9b2cf2;
    --dot-yellow: #ffe600;
    --dot-lilac: #d9b3f7;
    --bunny-light: #d49a63;
    --bunny-dark: #9a5f2c;
  }
  * { margin: 0; padding: 0; box-sizing: border-box; }
  html, body {
    width: 1200px; height: 800px; overflow: hidden;
    background: var(--stage);
  }
  .stage { position: relative; width: 1200px; height: 800px; }
  .book-cover {
    position: absolute; left: 350px; top: 30px;
    width: 500px; height: 740px;
    background: var(--paper);
    border-radius: 14px;
    overflow: hidden;
  }
  .book-cover svg { display: block; }
  .title-main {
    font-family: "Luckiest Guy", "Fredoka", sans-serif;
    font-size: 56px;
    fill: var(--title-pink);
    stroke: var(--title-navy);
    stroke-width: 5px;
    paint-order: stroke fill;
  }
  .title-sub {
    font-family: "Luckiest Guy", "Fredoka", sans-serif;
    font-size: 26px;
    fill: var(--title-navy);
    stroke: #ffffff;
    stroke-width: 3px;
    paint-order: stroke fill;
  }
  .age-text {
    font-family: "Fredoka", sans-serif;
    font-weight: 600;
    fill: var(--egg-text);
  }
  .band-text {
    font-family: "Fredoka", sans-serif;
    font-weight: 700;
    font-size: 19px;
    fill: var(--band-text);
    letter-spacing: 0.5px;
  }
  .edition-text {
    font-family: "Luckiest Guy", "Fredoka", sans-serif;
    font-size: 40px;
    fill: var(--title-navy);
    stroke: var(--title-pink);
    stroke-width: 4px;
    paint-order: stroke fill;
    letter-spacing: 1px;
  }
</style>
</head>
<body>
<main class="stage">
  <section class="book-cover">
    <svg width="500" height="740" viewBox="0 0 500 740" xmlns="http://www.w3.org/2000/svg">
      <defs>
        <path id="title-arc" d="M 45 175 Q 250 55 455 175"/>
        <path id="subtitle-arc" d="M 65 240 Q 250 130 435 240"/>
        <linearGradient id="bunny-fill" x1="0" y1="0" x2="0" y2="1">
          <stop offset="0" stop-color="var(--bunny-light)"/>
          <stop offset="1" stop-color="var(--bunny-dark)"/>
        </linearGradient>
      </defs>

      <g class="marker-dots">
        <circle cx="18" cy="92" r="26" fill="var(--dot-brown)"/>
        <circle cx="146" cy="18" r="30" fill="var(--dot-teal)" opacity="0.8"/>
        <circle cx="300" cy="30" r="30" fill="var(--dot-blush)"/>
        <circle cx="412" cy="12" r="22" fill="var(--dot-teal)"/>
        <circle cx="190" cy="248" r="28" fill="var(--dot-salmon)"/>
        <circle cx="350" cy="262" r="26" fill="var(--dot-green)"/>
        <circle cx="440" cy="300" r="32" fill="var(--dot-rust)"/>
        <circle cx="120" cy="300" r="30" fill="var(--dot-pink)"/>
        <circle cx="33" cy="340" r="30" fill="var(--dot-green)"/>
        <circle cx="115" cy="395" r="30" fill="var(--dot-maroon)"/>
        <circle cx="51" cy="460" r="32" fill="var(--dot-blue)"/>
        <circle cx="410" cy="414" r="32" fill="var(--dot-pink)"/>
        <circle cx="345" cy="380" r="26" fill="var(--dot-teal)"/>
        <circle cx="130" cy="540" r="32" fill="var(--dot-red)"/>
        <circle cx="60" cy="600" r="30" fill="var(--dot-purple)"/>
        <circle cx="355" cy="575" r="28" fill="var(--dot-pink)"/>
        <circle cx="20" cy="735" r="30" fill="var(--dot-yellow)"/>
        <circle cx="475" cy="720" r="30" fill="var(--dot-lilac)"/>
      </g>

      <rect class="cover-art" x="160" y="290" width="180" height="320" rx="88"
            fill="url(#bunny-fill)" role="img"
            aria-label="Cartoon Easter bunny standing and holding a carrot"/>

      <text class="title-main"><textPath href="#title-arc" startOffset="50%" text-anchor="middle" textLength="390" lengthAdjust="spacingAndGlyphs">DOT MARKERS</textPath></text>
      <text class="title-sub"><textPath href="#subtitle-arc" startOffset="50%" text-anchor="middle" textLength="350" lengthAdjust="spacingAndGlyphs">ACTIVITY BOOK FOR TODDLERS</textPath></text>

      <g class="age-badge">
        <ellipse cx="432" cy="532" rx="48" ry="60" fill="var(--egg-blue)"/>
        <text class="age-text" x="432" y="515" font-size="22" text-anchor="middle">AGES</text>
        <text class="age-text" x="432" y="540" font-size="18" text-anchor="middle">1-3, 2-4,</text>
        <text class="age-text" x="432" y="563" font-size="18" text-anchor="middle">3-5</text>
      </g>

      <g class="subtitle-band">
        <polygon points="0,630 500,610 500,656 0,676" fill="var(--band-pink)"/>
        <text class="band-text" x="250" y="650" text-anchor="middle" transform="rotate(-2.3 250 643)">PIP-N-STAMP CHILDREN'S EASTR BOOK FOR KIDS</text>
      </g>

      <text class="edition-text" x="250" y="722" text-anchor="middle">EASTER EDITION</text>
    </svg>
  </section>
</main>
</body>
</html>
```